" Incluímos agricultores familiares na cadeia de valor agropecuárias de empresa e cooperativas com viabilidade e sustentabilidade. O nosso foco è resiliência climática do produtur "

```html
<!DOCTYPE html>
<html lang="pt-BR">
<head>
<meta charset="utf-8">
<title>Campo Vivo – Capa de página</title>
<link href="https://fonts.googleapis.com/css2?family=Open+Sans:wght@400;600;700;800&display=swap" rel="stylesheet">
<style>
  :root {
    --page-bg: #eef0f2;
    --panel: #ffffff;
    --navy: #1f3f8c;
    --navy-dark: #17306e;
    --text: #3a3a3a;
    --border: #d8dbe0;
    --field-green: #7f9462;
    --field-earth: #a08a6b;
    --sky: #dfe6ea;
  }
  * { box-sizing: border-box; margin: 0; padding: 0; }
  html, body { width: 1200px; height: 1200px; overflow: hidden; }
  body {
    background: var(--page-bg);
    font-family: "Open Sans", Arial, sans-serif;
    position: relative;
  }
  .profile-card {
    position: absolute;
    left: 60px; top: 440px;
    width: 190px; height: 190px;
    background: var(--panel);
    border: 1px solid var(--border);
    display: flex; align-items: center; justify-content: center;
    gap: 10px;
  }
  .brand-name {
    font-weight: 800;
    color: var(--navy);
    letter-spacing: 0.5px;
    white-space: nowrap;
  }
  .profile-card .brand-name { font-size: 22px; }
  .brand-dot {
    width: 16px; height: 16px; border-radius: 50%;
    background: #f0a020;
  }
  .cover {
    position: absolute;
    left: 255px; top: 430px;
    width: 885px; height: 340px;
    background: var(--panel);
    border: 1px solid var(--border);
    overflow: hidden;
  }
  .cover-photo {
    position: absolute; right: 0; top: 0;
    width: 520px; height: 100%;
    background: linear-gradient(160deg, var(--sky) 0%, #b9c2a6 35%, var(--field-green) 60%, var(--field-earth) 100%);
  }
  .cover-fade {
    position: absolute; right: 300px; top: 0;
    width: 220px; height: 100%;
    background: linear-gradient(90deg, var(--panel), rgba(255,255,255,0));
  }
  .icon-bar {
    position: absolute; left: 0; top: 100px;
    width: 40px; bottom: 0;
    background: var(--navy);
    display: flex; flex-direction: column; align-items: center;
    padding-top: 68px; gap: 26px;
  }
  .icon-bar svg { width: 18px; height: 18px; fill: #fff; }
  .contact {
    position: absolute; left: 56px; top: 88px;
    color: var(--text);
  }
  .contact h1 {
    font-size: 31px; font-weight: 600; color: var(--navy-dark);
    margin-bottom: 26px;
  }
  .contact p { font-size: 17px; line-height: 1.2; margin-bottom: 20px; }
  .contact .address { font-size: 14.5px; line-height: 1.35; }
  .cover .brand {
    position: absolute; left: 330px; top: 170px;
    display: flex; align-items: center; gap: 14px;
  }
  .cover .brand-name { font-size: 48px; }
  .cover .brand-dot { width: 34px; height: 34px; }
</style>
</head>
<body>
  <div class="profile-card">
    <span class="brand-dot"></span>
    <span class="brand-name">Campo Vivo</span>
  </div>

  <section class="cover">
    <div class="cover-photo" role="img" aria-label="Fotografia de agricultor com chapéu colhendo hortaliças e tomates em uma caixa na horta"></div>
    <div class="cover-fade"></div>

    <div class="icon-bar">
      <svg viewBox="0 0 24 24"><path d="M6.6 10.8a15.1 15.1 0 0 0 6.6 6.6l2.2-2.2a1 1 0 0 1 1-.25 11.4 11.4 0 0 0 3.6.57 1 1 0 0 1 1 1V20a1 1 0 0 1-1 1A17 17 0 0 1 3 4a1 1 0 0 1 1-1h3.5a1 1 0 0 1 1 1c0 1.25.2 2.45.57 3.6a1 1 0 0 1-.25 1z"/></svg>
      <svg viewBox="0 0 24 24"><circle cx="12" cy="12" r="10"/></svg>
      <svg viewBox="0 0 24 24"><path d="M2 5h20v14H2z M3.5 6.5 12 13l8.5-6.5" fill="none" stroke="#fff" stroke-width="2"/></svg>
      <svg viewBox="0 0 24 24"><path d="M12 2a7 7 0 0 0-7 7c0 5.2 7 13 7 13s7-7.8 7-13a7 7 0 0 0-7-7zm0 9.5A2.5 2.5 0 1 1 12 6.5a2.5 2.5 0 0 1 0 5z"/></svg>
    </div>

    <div class="contact">
      <h1>Contato</h1>
      <p>(31) 3555-0142</p>
      <p>(31) 95555-0187</p>
      <p>contato@campovivo.com.br</p>
      <p class="address">Rua das Palmeiras, Nº 120 - Bairro<br>Cidade/UF CEP: 35420-000</p>
    </div>

    <div class="brand">
      <span class="brand-dot"></span>
      <span class="brand-name">Campo Vivo</span>
    </div>
  </section>
</body>
</html>
```